Coconut Oil - FOOD Label Design

We have a label design for Coconut oil jars in 2 sizes with stickers for the lids. The bottles are clear, oil is white. Label Size: 217 x 52 mm (Width x Height), Lid ø 50 mm and 268 x 70 mm (Width x Height), Lid ø70 maximum Peel back label is necessary in four languages, engl. in front F, NL, D on the back Brand logo is "velunta". Logo is attached to the AI ​​file We need open Adobe Illustrator files including graphics, photos and fonts. See attached file including all the texts, logos and the cut, with the the cut you can vary as long as you are in the size , hair and body "etc Coconut Oil - FOOD - 200 g to 500 g Responsible Person EAN code - see attached file is in the AI-file

Target Market(s)

european customers

Requirements
Must have
• Velunta logo
Nice to have
• selling points

```html
<!DOCTYPE html>
<html lang="en">
<head>
<meta charset="utf-8">
<title>Velunta Coconut Oil Food Label</title>
<link href="https://fonts.googleapis.com/css2?family=Cinzel:wght@700&family=Arimo:wght@700&family=Tinos&family=Nunito:wght@600&display=swap" rel="stylesheet">
<style>
  :root {
    --field-green: #76b82a;
    --crown-green: #5da323;
    --band-lime: #b0cc24;
    --brand-green: #79b52e;
    --title-grey: #4a4a4a;
    --paper: #ffffff;
    --nut-brown: #8a5a32;
    --leaf-green: #4f8f2a;
  }
  html, body {
    margin: 0;
    padding: 0;
    width: 1200px;
    height: 454px;
    overflow: hidden;
    background: var(--field-green);
  }
  .canvas {
    position: relative;
    width: 1200px;
    height: 454px;
    background: var(--field-green);
  }
  .label {
    position: absolute;
    left: 313px;
    top: 0;
    width: 577px;
    height: 454px;
    overflow: hidden;
  }
  .label-shape {
    position: absolute;
    inset: 0;
  }
  .pack-size {
    position: absolute;
    left: 45px;
    top: 26px;
    margin: 0;
    font-family: "Tinos", serif;
    font-size: 17px;
    color: var(--paper);
  }
  .brand {
    position: absolute;
    left: 0;
    width: 577px;
    top: 24px;
    text-align: center;
  }
  .brand-dot {
    display: block;
    width: 72px;
    height: 72px;
    margin: 0 auto;
    border-radius: 50%;
    background: var(--paper);
  }
  .brand-name {
    display: block;
    margin-top: 18px;
    font-family: "Nunito", sans-serif;
    font-weight: 600;
    font-size: 34px;
    line-height: 1;
    color: var(--brand-green);
  }
  .product-title {
    position: absolute;
    left: 0;
    width: 577px;
    top: 186px;
    margin: 0;
    text-align: center;
    font-family: "Cinzel", serif;
    font-weight: 700;
    font-size: 36px;
    line-height: 48px;
    letter-spacing: 0.5px;
    color: var(--title-grey);
  }
  .selling-points {
    position: absolute;
    left: 33px;
    top: 250px;
    margin: 0;
    font-family: "Arimo", sans-serif;
    font-weight: 700;
    font-size: 25px;
    line-height: 37px;
    color: var(--brand-green);
  }
  .coconut-visual {
    position: absolute;
    left: 318px;
    top: 250px;
    width: 250px;
    height: 150px;
    border-radius: 40% 40% 14px 14px;
    background: radial-gradient(circle at 55% 45%, #f4efe6 0%, #c89c6c 38%, var(--nut-brown) 66%, var(--leaf-green) 100%);
  }
  .net-weight {
    position: absolute;
    left: 36px;
    top: 418px;
    margin: 0;
    font-family: "Tinos", serif;
    font-size: 21px;
    color: #1f1f1f;
  }
</style>
</head>
<body>
  <main class="canvas">
    <section class="label">
      <svg class="label-shape" width="577" height="454" viewBox="0 0 577 454" aria-hidden="true">
        <rect width="577" height="454" fill="var(--paper)"/>
        <path d="M0 0 H577 V62 C420 66 260 104 0 124 Z" fill="var(--crown-green)"/>
        <rect x="0" y="403" width="577" height="51" fill="var(--band-lime)"/>
      </svg>

      <p class="pack-size">Pack size : 2ltr</p>

      <div class="brand">
        <span class="brand-dot"></span>
        <span class="brand-name">velunta</span>
      </div>

      <h1 class="product-title">COCONUT-OIL-FOOD</h1>

      <p class="selling-points">Pure, virgin organic,<br>suitable for kitchen,<br>hair and body</p>

      <div class="coconut-visual" role="img" aria-label="Photo of whole and halved coconuts on green palm leaves"></div>

      <p class="net-weight">Nt.Wt.200g</p>
    </section>
  </main>
</body>
</html>
```